Presentation Folder, Business Card, Letterhead and Envelope design

We are a dental clinic that will open in August and we are looking for a professional graphic designer to create our Business Card, Presentation Folder, Letterhead, Notepad and envelopes.

The brand LumaGrin must reflect a sense of quality and sophistication, marketed for middle-class consumers.
Our preference is for quality and refined materials, where less is more.
Attached the logo

```html
<!DOCTYPE html>
<html lang="en">
<head>
<meta charset="utf-8">
<title>LumaGrin Stationery</title>
<link href="https://fonts.googleapis.com/css2?family=Abel&family=Lato:wght@400;700;900&family=Montserrat:wght@400&display=swap" rel="stylesheet">
<style>
  :root {
    --backdrop: #d8e3ee;
    --paper: #ffffff;
    --brand-red: #650f12;
    --brand-grey: #58585a;
    --ink: #4a4a4a;
    --ink-soft: #5c5c5c;
  }
  * { margin: 0; padding: 0; box-sizing: border-box; }
  html, body { width: 1200px; height: 831px; overflow: hidden; }
  body { background: var(--backdrop); position: relative; font-family: "Lato", sans-serif; color: var(--ink); }

  .sheet { position: absolute; background: var(--paper); box-shadow: 0 2px 8px rgba(60,80,100,.28); }
  .abs { position: absolute; }

  .wordmark { position: absolute; display: flex; align-items: center; font-family: "Montserrat", sans-serif; font-weight: 400; color: var(--ink); white-space: nowrap; }
  .wordmark .mark-square { background: var(--brand-grey); flex: none; }
  .wordmark.on-red { color: #fff; }
  .wordmark.on-red .mark-square { background: #fff; }

  .contact { position: absolute; font-family: "Lato", sans-serif; color: var(--ink-soft); white-space: nowrap; }
  .contact p { display: flex; align-items: center; }
  .contact svg { fill: var(--brand-red); flex: none; }

  .footer-band { position: absolute; background: var(--brand-red); }
  .footer-tab { position: absolute; background: var(--brand-grey); }

  /* letterhead */
  .letterhead { left: 117px; top: 111px; width: 430px; height: 609px; }
  .letter-body { position: absolute; left: 39px; top: 178px; width: 349px; font-family: "Abel", sans-serif; font-size: 9.4px; line-height: 15px; color: var(--ink); text-align: justify; }
  .letter-body p { margin-bottom: 15px; }
  .letter-body .salutation { margin-bottom: 13px; }
  .closing { position: absolute; left: 39px; top: 484px; font-family: "Abel", sans-serif; font-size: 9.4px; color: var(--ink); }
  .signature { position: absolute; left: 37px; top: 504px; width: 36px; height: 23px; background: linear-gradient(90deg, rgba(101,15,18,.15), rgba(101,15,18,.35)); border-radius: 3px; }

  /* business card */
  .card-front { left: 635px; top: 112px; width: 183px; height: 105px; }
  .card-divider { position: absolute; left: 97px; top: 26px; width: 1px; height: 53px; background: var(--brand-red); }
  .card-person { position: absolute; left: 107px; top: 25px; }
  .card-person .name { font-weight: 900; font-size: 8.6px; color: var(--brand-red); letter-spacing: .1px; }
  .card-person .role { font-size: 4.8px; color: var(--ink-soft); margin-top: 1px; }
  .card-back { left: 904px; top: 111px; width: 182px; height: 104px; background: var(--brand-red); }

  /* envelope back */
  .envelope-back { left: 635px; top: 248px; width: 451px; height: 225px; }
  .envelope-flap { position: absolute; left: 0; top: 0; }

  /* envelope front */
  .envelope-front { left: 635px; top: 494px; width: 451px; height: 226px; }
</style>
</head>
<body>

<svg width="0" height="0" style="position:absolute">
  <defs>
    <symbol id="icon-phone" viewBox="0 0 16 16"><path d="M3.6 1.2l2.3 2.3-1.4 2a9 9 0 0 0 6 6l2-1.4 2.3 2.3-1.6 2.2C7.4 14.7 1.3 8.6 1.4 2.8z"/></symbol>
    <symbol id="icon-mail" viewBox="0 0 16 16"><path d="M1 3h14v10H1z M2.2 4.2v.5L8 8.6l5.8-3.9v-.5z" fill-rule="evenodd"/></symbol>
    <symbol id="icon-globe" viewBox="0 0 16 16"><path d="M8 1a7 7 0 1 0 0 14A7 7 0 0 0 8 1zm0 1.3c.9 0 1.8 1.9 2 4.7H6c.2-2.8 1.1-4.7 2-4.7zM2.4 7h2.4c.1-1.6.4-3 .9-4A5.7 5.7 0 0 0 2.4 7zm8.8 0h2.4a5.7 5.7 0 0 0-3.3-4c.5 1 .8 2.4.9 4zM2.4 9a5.7 5.7 0 0 0 3.3 4c-.5-1-.8-2.4-.9-4zm3.6 0c.2 2.8 1.1 4.7 2 4.7s1.8-1.9 2-4.7zm5.2 0c-.1 1.6-.4 3-.9 4a5.7 5.7 0 0 0 3.3-4z"/></symbol>
  </defs>
</svg>

<!-- Letterhead -->
<section class="sheet letterhead">
  <div class="wordmark" style="left:39px;top:44px;font-size:21px;letter-spacing:5.2px;gap:6px;">
    <span class="mark-square" style="width:20px;height:20px;"></span>LumaGrin
  </div>
  <div class="contact" style="left:326px;top:29px;font-size:7.3px;line-height:8.7px;">
    <p>1234 First Line Address</p>
    <p>5678 Second Line Address</p>
    <p style="margin-top:4px;line-height:10px;"><svg width="7" height="7" style="margin-right:6px"><use href="#icon-phone"/></svg>(111) 999-0000</p>
    <p style="line-height:10px;"><svg width="7" height="7" style="margin-right:6px"><use href="#icon-mail"/></svg>Info@yourmail.com</p>
    <p style="line-height:10px;"><svg width="7" height="7" style="margin-right:6px"><use href="#icon-globe"/></svg>www.yourwesite.com</p>
  </div>
  <div class="letter-body">
    <p class="salutation">Dear Sir/Mam,</p>
    <p>Contrary to popular belief, Lorem Ipsum is not simply random text. It has roots in a piece of classical Latin literature from 45 BC, making it over 2000 years old. Edwin Harlow, a Latin professor at Ashford-Vale College in Virginia, looked up one of the more obscure Latin words, consectetur.</p>
    <p>Lorem Ipsum comes from sections 1.10.32 and 1.10.33 of "de Finibus Bonorum et Malorum" (The Extremes of Good and Evil) by Lucan Aurel, written in 45 BC. This book is a treatise on the theory of ethics, very popular during the Renaissance. The first line of Lorem Ipsum.</p>
    <p>The standard chunk of Lorem Ipsum used since the 1500s is reproduced below for those interested. Sections 1.10.32 and 1.10.33 from "de Finibus Bonorum et Malorum" by Lucan Aurel are also reproduced in their exact original.</p>
    <p>The standard chunk of Lorem Ipsum used since the 1500s is reproduced below for those interested.</p>
  </div>
  <p class="closing">Best Regards</p>
  <div class="signature" role="img" aria-label="Handwritten signature of the sender"></div>
  <div class="footer-band" style="left:0;top:578px;width:354px;height:13px;"></div>
  <div class="footer-tab" style="left:362px;top:572px;width:24px;height:24px;"></div>
  <div class="footer-tab" style="left:393px;top:578px;width:37px;height:13px;"></div>
</section>

<!-- Business card, front -->
<section class="sheet card-front">
  <div class="wordmark" style="left:10px;top:47px;font-size:9.6px;letter-spacing:2.2px;gap:3px;">
    <span class="mark-square" style="width:9px;height:9px;"></span>LumaGrin
  </div>
  <div class="card-divider"></div>
  <div class="card-person">
    <p class="name">DANIEL REYES</p>
    <p class="role">Founder</p>
  </div>
  <div class="contact" style="left:107px;top:46px;font-size:4.7px;line-height:6px;">
    <p>1234 First Line Address</p>
    <p>5678 Second Line Address</p>
    <p style="margin-top:3px;line-height:7px;"><svg width="5" height="5" style="margin-right:4px"><use href="#icon-phone"/></svg>1234567890</p>
    <p style="line-height:7px;"><svg width="5" height="5" style="margin-right:4px"><use href="#icon-mail"/></svg>info@yourmail.com</p>
    <p style="line-height:7px;"><svg width="5" height="5" style="margin-right:4px"><use href="#icon-globe"/></svg>www.yourwebsite.com</p>
  </div>
  <div class="footer-band" style="left:0;top:93px;width:150px;height:6px;"></div>
  <div class="footer-tab" style="left:154px;top:91px;width:11px;height:10px;"></div>
  <div class="footer-tab" style="left:168px;top:93px;width:15px;height:6px;"></div>
</section>

<!-- Business card, back -->
<section class="sheet card-back">
  <div class="wordmark on-red" style="left:32px;top:44px;font-size:13.5px;letter-spacing:3px;gap:5px;">
    <span class="mark-square" style="width:14px;height:14px;"></span>LumaGrin
  </div>
</section>

<!-- Envelope, back -->
<section class="sheet envelope-back">
  <svg class="envelope-flap" width="451" height="66" viewBox="0 0 451 66">
    <path d="M0 0H451L447 35Q444 66 413 66H38Q7 66 4 35Z" fill="var(--brand-red)"/>
  </svg>
  <div class="wordmark on-red" style="left:0;width:451px;justify-content:center;top:23px;font-size:13px;letter-spacing:2.6px;">LumaGrin</div>
  <div class="wordmark" style="left:0;width:451px;justify-content:center;top:196px;font-size:11px;letter-spacing:3px;">LumaGrin</div>
</section>

<!-- Envelope, front -->
<section class="sheet envelope-front">
  <div class="wordmark" style="left:39px;top:43px;font-size:26px;letter-spacing:6.4px;gap:7px;">
    <span class="mark-square" style="width:25px;height:25px;"></span>LumaGrin
  </div>
  <div class="contact" style="left:42px;top:132px;font-size:7.3px;line-height:8.8px;">
    <p>1234 First Line Address</p>
    <p>5678 Second Line Address</p>
    <p style="margin-top:4px;line-height:10px;"><svg width="7" height="7" style="margin-right:6px"><use href="#icon-phone"/></svg>(111) 999-0000</p>
    <p style="line-height:10px;"><svg width="7" height="7" style="margin-right:6px"><use href="#icon-mail"/></svg>Info@yourmail.com</p>
    <p style="line-height:10px;"><svg width="7" height="7" style="margin-right:6px"><use href="#icon-globe"/></svg>www.yourwesite.com</p>
  </div>
  <div class="footer-band" style="left:0;top:198px;width:372px;height:14px;"></div>
  <div class="footer-tab" style="left:381px;top:193px;width:25px;height:24px;"></div>
  <div class="footer-tab" style="left:413px;top:198px;width:38px;height:14px;"></div>
</section>

</body>
</html>
```